Birchline Septic Solutions

Would like to see some single sided ones but would also like to see some double sided with one sided only being the logo. Owners name is Tom Halvick. Phone number is 555-214-0387
Services are pumping, inspections, installs, and repairs

Contact Information for Business Card

555-241-0387 Tom Halvick Harlow Ridge, OH

```html
<!DOCTYPE html>
<html lang="en">
<head>
<meta charset="utf-8">
<title>Birchline Septic Solutions – Business Card</title>
<link rel="stylesheet" href="https://fonts.googleapis.com/css2?family=Montserrat:wght@500;600;700;800&display=swap">
<style>
  :root {
    --page-bg: #e9e3da;
    --card-top: #f4f6f7;
    --card-bottom: #e6e9ea;
    --card-edge: rgba(255, 255, 255, 0.9);
    --ink-dark: #1f1f1f;
    --ink-grey: #3c3c3c;
    --accent-teal: #22b5a4;
  }
  * { margin: 0; padding: 0; box-sizing: border-box; }
  html, body {
    width: 1200px;
    height: 897px;
    overflow: hidden;
    background: var(--page-bg);
    font-family: "Montserrat", Arial, sans-serif;
  }
  .canvas {
    position: relative;
    width: 1200px;
    height: 897px;
    display: flex;
    align-items: center;
    justify-content: center;
  }
  .business-card {
    position: relative;
    width: 1000px;
    height: 547px;
    border-radius: 26px;
    background: linear-gradient(160deg, var(--card-top), var(--card-bottom));
    border: 2px solid var(--card-edge);
    box-shadow: 0 18px 40px rgba(80, 60, 40, 0.18);
    overflow: hidden;
  }
  .brand-name {
    position: absolute;
    right: 42px;
    top: 120px;
    width: 340px;
    text-align: center;
    color: var(--ink-dark);
    font-weight: 800;
    text-transform: uppercase;
    line-height: 1;
  }
  .brand-name__main {
    display: block;
    font-size: 56px;
    letter-spacing: 1px;
  }
  .brand-name__sub {
    display: block;
    margin-top: 18px;
    font-size: 19px;
    letter-spacing: 5px;
  }
  .contact {
    position: absolute;
    left: 50px;
    top: 330px;
  }
  .contact__name {
    color: var(--accent-teal);
    font-size: 54px;
    font-weight: 700;
    letter-spacing: 1px;
    line-height: 1;
    text-transform: uppercase;
  }
  .contact__location {
    margin-top: 14px;
    color: var(--ink-grey);
    font-size: 34px;
    font-weight: 600;
    line-height: 1;
  }
  .contact__phone {
    margin-top: 26px;
    display: flex;
    align-items: center;
    gap: 16px;
    color: var(--ink-grey);
    font-size: 46px;
    font-weight: 500;
    line-height: 1;
    letter-spacing: 1px;
  }
  .contact__phone-icon {
    width: 36px;
    height: 30px;
    fill: var(--accent-teal);
  }
</style>
</head>
<body>
<main class="canvas">
  <section class="business-card" aria-label="Birchline Septic Solutions business card">
    <h1 class="brand-name">
      <span class="brand-name__main">Birchline</span>
      <span class="brand-name__sub">Septic Solutions</span>
    </h1>

    <div class="contact">
      <p class="contact__name">Tom Halvick</p>
      <p class="contact__location">Harlow Ridge, OH</p>
      <p class="contact__phone">
        <svg class="contact__phone-icon" viewBox="0 0 36 30" aria-hidden="true">
          <path d="M2 10c0-5 7-8 16-8s16 3 16 8v3h-8v-4c-2-1-5-1.5-8-1.5S12 8 10 9v4H2z"/>
          <path d="M9 14l3-4h12l3 4 5 14H4z"/>
          <g fill="#ffffff">
            <rect x="12" y="16" width="3" height="2.5"/>
            <rect x="16.5" y="16" width="3" height="2.5"/>
            <rect x="21" y="16" width="3" height="2.5"/>
            <rect x="12" y="20" width="3" height="2.5"/>
            <rect x="16.5" y="20" width="3" height="2.5"/>
            <rect x="21" y="20" width="3" height="2.5"/>
          </g>
        </svg>
        <span>555-241-0387</span>
      </p>
    </div>
  </section>
</main>
</body>
</html>
```